New home maintenance business, on the back of business card i would like dot points of my services provided.
these include,
General household repairs and maintenance
Painting
Verolin/Plaster Repairs
Fencing
Gardening and landscaping
Cleaning and removals
Doors and windows
Hinges and Locks
Fly screen/ screen door Repairs
I like black,silver, red but ill leav it up to you guys as something may be better for business.. , would also it be possible to create a logo for me incorporating the K&T as i want to make up t shirts in future thankyou
i would also like to put Marco Vintelli on the cards aswell please, and on back change painter to proffesional painter and decorator, please
i like alot of the designs sofar, i cant put my finger on wat 1 yet though!! cheers guys
Business
K&T HOME MAINTENANCE SERVICES
Lewis Vintelli 0467205184
kntmaintenance@postvale.com
ABN:57140328619

```html
<!DOCTYPE html>
<html lang="en">
<head>
<meta charset="utf-8">
<title>K&amp;T Home Maintenance Services – Business Card</title>
<link href="https://fonts.googleapis.com/css2?family=Arimo:wght@400;700&display=swap" rel="stylesheet">
<style>
  :root {
    --page: #ffffff;
    --ink: #1d1d1d;
    --label: #3a3a3a;
    --charcoal-top: #6b6b6b;
    --charcoal-mid: #3a3a3a;
    --charcoal-deep: #1c1c1c;
    --silver: #e9e9e9;
    --silver-dark: #bdbdbd;
    --red: #d2151f;
    --white: #ffffff;
  }
  * { box-sizing: border-box; margin: 0; padding: 0; }
  html, body {
    width: 841px; height: 1200px; overflow: hidden;
    background: var(--page);
    font-family: "Arimo", Arial, sans-serif;
  }
  .sheet { position: relative; width: 841px; height: 1200px; }

  .side-label {
    position: absolute; left: 40px;
    font-size: 19px; color: var(--label);
  }

  .card {
    position: absolute; left: 248px; width: 566px; height: 350px;
    border-radius: 16px; overflow: hidden;
    background: var(--white);
    box-shadow: 0 2px 6px rgba(0,0,0,.25);
  }
  .card--front { top: 14px; }
  .card--back-one { top: 428px; }
  .card--back-two { top: 836px; }

  .card__dark {
    position: absolute; left: 0; top: 0; width: 100%;
    background: radial-gradient(ellipse at 55% 0%, var(--charcoal-top) 0%, var(--charcoal-mid) 55%, var(--charcoal-deep) 100%);
  }
  .card--front .card__dark { height: 188px; }
  .card--back-one .card__dark { height: 202px; }
  .card--back-two .card__dark { height: 196px; }

  .card__trades {
    position: absolute; left: 16px; right: 16px; bottom: 14px; height: 82px;
    background: linear-gradient(180deg, var(--silver) 0%, var(--silver-dark) 100%);
    border-radius: 4px;
  }
  .card__strip {
    position: absolute; left: 0; right: 0; bottom: 0; height: 8px;
    background: var(--red);
  }

  .brand {
    position: absolute;
    display: flex; align-items: center; gap: 10px;
    color: var(--red); font-weight: 700;
  }
  .brand__mark { width: 22px; height: 22px; background: var(--red); flex: none; }
  .brand__name { line-height: 1.05; text-transform: uppercase; }
  .brand__initials { display: block; font-size: 34px; }
  .brand__words { display: block; font-size: 11px; letter-spacing: .3px; }

  .card--front .brand { left: 34px; top: 196px; }
  .card--back-one .brand { left: 340px; top: 206px; }
  .card--back-two .brand { left: 340px; top: 200px; }

  .contact {
    position: absolute; left: 300px; top: 26px;
    color: var(--white);
  }
  .contact__names { font-size: 19px; margin-bottom: 14px; }
  .contact__row {
    display: flex; align-items: center; gap: 9px;
    font-size: 15px; margin-bottom: 11px;
  }
  .contact__row svg { width: 16px; height: 16px; flex: none; }
  .contact__abn { font-size: 14px; font-weight: 700; margin-top: 6px; }

  .services {
    position: absolute; left: 34px;
    list-style: none; color: var(--white);
    font-size: 14.5px; line-height: 19.5px;
  }
  .card--back-one .services { top: 16px; }
  .card--back-two .services { top: 12px; }
  .services li { position: relative; padding-left: 18px; }
  .services li::before {
    content: ""; position: absolute; left: 0; top: 7px;
    width: 6px; height: 6px; border-radius: 50%;
    background: var(--red);
  }
</style>
</head>
<body>
<main class="sheet">

  <span class="side-label" style="top:176px;">front</span>
  <section class="card card--front">
    <div class="card__dark"></div>
    <div class="contact">
      <p class="contact__names">Lewis Vintelli &amp; Marco Vintelli</p>
      <p class="contact__row">
        <svg viewBox="0 0 16 16" aria-hidden="true"><rect x="1" y="1" width="14" height="14" rx="2" fill="#d2151f"/><path d="M5 4.2c.5-.4 1-.3 1.3.2l.7 1.2c.2.4.1.8-.2 1l-.5.4c.4 1 1.2 1.8 2.2 2.2l.4-.5c.3-.3.7-.4 1-.2l1.2.7c.5.3.6.8.2 1.3-.7.9-1.7 1.1-2.7.6C6.9 10.3 5.7 9.1 4.9 7.4c-.5-1-.4-2.3.1-3.2z" fill="#fff"/></svg>
        0467205184
      </p>
      <p class="contact__row">
        <svg viewBox="0 0 16 16" aria-hidden="true"><rect x="1" y="1" width="14" height="14" rx="2" fill="#d2151f"/><rect x="3.5" y="5" width="9" height="6.5" fill="none" stroke="#fff" stroke-width="1.1"/><path d="M3.5 5l4.5 3.6L12.5 5" fill="none" stroke="#fff" stroke-width="1.1"/></svg>
        kntmaintenance@postvale.com
      </p>
      <p class="contact__abn">ABN: 57140328619</p>
    </div>
    <div class="brand">
      <span class="brand__mark"></span>
      <span class="brand__name"><span class="brand__initials">K&amp;T</span><span class="brand__words">Home Maintenance Services</span></span>
    </div>
    <div class="card__trades" role="img" aria-label="Row of black silhouettes of tradespeople at work: painting, gardening, carrying tools and ladders"></div>
    <div class="card__strip"></div>
  </section>

  <span class="side-label" style="top:590px;">back 1</span>
  <section class="card card--back-one">
    <div class="card__dark"></div>
    <ul class="services">
      <li>General household repairs and maintenance</li>
      <li>Proffesional painter and decorator</li>
      <li>Verolin/Plaster Repairs</li>
      <li>Fencing</li>
      <li>Gardening and landscaping</li>
      <li>Cleaning and removals</li>
      <li>Doors and windows</li>
      <li>Hinges and Locks</li>
      <li>Fly screen/ screen door Repairs</li>
    </ul>
    <div class="brand">
      <span class="brand__mark"></span>
      <span class="brand__name"><span class="brand__initials">K&amp;T</span><span class="brand__words">Home Maintenance Services</span></span>
    </div>
    <div class="card__trades" role="img" aria-label="Row of black silhouettes of tradespeople at work: painting, gardening, carrying tools and ladders"></div>
    <div class="card__strip"></div>
  </section>

  <span class="side-label" style="top:1000px;">back 2</span>
  <section class="card card--back-two">
    <div class="card__dark"></div>
    <ul class="services">
      <li>General household repairs and maintenance</li>
      <li>Proffesional painter and decorator</li>
      <li>Verolin/Plaster Repairs</li>
      <li>Fencing</li>
      <li>Gardening and landscaping</li>
      <li>Cleaning and removals</li>
      <li>Doors and windows</li>
      <li>Hinges and Locks</li>
      <li>Fly screen/ screen door Repairs</li>
    </ul>
    <div class="brand">
      <span class="brand__mark"></span>
      <span class="brand__name"><span class="brand__initials">K&amp;T</span><span class="brand__words">Home Maintenance Services</span></span>
    </div>
    <div class="card__trades" role="img" aria-label="Row of black silhouettes of tradespeople at work: painting, gardening, carrying tools and ladders"></div>
    <div class="card__strip"></div>
  </section>

</main>
</body>
</html>
```